CHRISTMAS CARD

We want a Christmas card for wealth managers to issue to high net worth clients. Very classy. Very corporate. The finished printed card will be a5 to fit existing envelopes. the design will also be used as part of a digital card so i need the image in a format for email as well as print. The brand uses a silver (foil block) on its logo and a specific pan tone ref olive green (reference 620). Not too religious and include a quirky message.

Target Market(s)

The target market is clients with investments. Typically more than £100,000 which is why the card needs to be very classy.

Industry/Entity Type

Religious

Requirements
Must have
• logo - but i can't work out how to attach it! i can email it tho. contact me on mira@tarvexlink.com

```html
<!DOCTYPE html>
<html lang="en">
<head>
<meta charset="utf-8">
<title>Christmas Card – Ardmore Partners</title>
<link rel="stylesheet" href="https://fonts.googleapis.com/css2?family=Pinyon+Script&family=Montserrat:wght@400&display=swap">
<style>
  :root {
    --paper: #ffffff;
    --olive: #7b6c10;
    --festive-red: #ec1c24;
    --ink-light: #ffffff;
    --script: "Pinyon Script", cursive;
    --sans: "Montserrat", sans-serif;
  }
  html, body {
    margin: 0;
    padding: 0;
    width: 1200px;
    height: 1000px;
    overflow: hidden;
    background: var(--paper);
  }
  .canvas {
    position: relative;
    width: 1200px;
    height: 1000px;
  }
  .card {
    position: absolute;
    left: 287px;
    width: 620px;
    overflow: hidden;
    color: var(--ink-light);
  }
  .card--front {
    top: 18px;
    height: 437px;
    background: var(--olive);
  }
  .card--inside {
    top: 544px;
    height: 436px;
    background: var(--festive-red);
  }
  .script {
    position: absolute;
    margin: 0;
    font-family: var(--script);
    font-weight: 400;
    line-height: 1;
    white-space: nowrap;
  }
  .greeting-merry {
    left: 36px;
    top: 58px;
    font-size: 160px;
  }
  .greeting-christmas {
    left: 26px;
    top: 212px;
    font-size: 134px;
  }
  .footer-band {
    position: absolute;
    left: 0;
    bottom: 0;
    width: 100%;
    height: 77px;
    background: var(--festive-red);
  }
  .brand {
    position: absolute;
    left: 20px;
    top: 14px;
    width: 208px;
    text-align: center;
  }
  .brand-mark {
    display: block;
    width: 10px;
    height: 10px;
    margin: 0 auto 8px;
    border: 1.5px solid var(--ink-light);
    border-radius: 50%;
  }
  .brand-name {
    display: block;
    font-family: var(--sans);
    font-size: 13px;
    letter-spacing: 3px;
    line-height: 1;
    white-space: nowrap;
    padding-bottom: 7px;
    border-bottom: 1px solid var(--ink-light);
  }
  .wish-line {
    left: 33px;
    top: 26px;
    font-size: 58px;
  }
  .wish-happiness {
    left: 30px;
    top: 114px;
    font-size: 128px;
  }
  .wish-amp {
    left: 540px;
    top: 168px;
    font-size: 62px;
  }
  .wish-prosperity {
    left: 112px;
    top: 280px;
    font-size: 122px;
  }
</style>
</head>
<body>
  <main class="canvas">
    <section class="card card--front" aria-label="Card front">
      <h1 class="script greeting-merry">Merry</h1>
      <p class="script greeting-christmas">Christmas</p>
      <div class="footer-band">
        <div class="brand">
          <span class="brand-mark" aria-hidden="true"></span>
          <span class="brand-name">ARDMORE PARTNERS</span>
        </div>
      </div>
    </section>

    <section class="card card--inside" aria-label="Card message">
      <p class="script wish-line">we wish you find the key to</p>
      <p class="script wish-happiness">Happiness</p>
      <p class="script wish-amp">&amp;</p>
      <p class="script wish-prosperity">Prosperity</p>
    </section>
  </main>
</body>
</html>
```